Film Noir Cover Design - "Lanterns Over Quiet Water"

We're looking for a "Film Noir" styled book cover design. The book is a
biography of the life of Mabel Trusk. From humble beginnings in the urban
streets of Jersey City to entrepreneur in the High Tech world of Data centers.

The Title is: "Lanterns Over Quiet Water" (the life of Mabel Trusk)

Somewhere prominently, we'd like to include the following three lines of dialog from the movie Veradomo:

Hal: Has it got a wow finish?
Greta: I don't know the finish yet.
Hal: Well, go on. Tell it - maybe one will come to you as you go along.

Be creative and have fun. Try to capture the excitement of a progressive life well lived. The imagery should be positive and upbeat,

Target Market(s)

Woman looking for an inspirational story of a life of success and accomplishment.

Colors

Designer to choose colors to be used in the design.

Requirements
Must have
• Positive, up beat imagery -- that maintains thew "Film Noir" image style.

```html
<!DOCTYPE html>
<html lang="en">
<head>
<meta charset="utf-8">
<title>Lanterns Over Quiet Water — The life of Mabel Trusk</title>
<link rel="stylesheet" href="https://fonts.googleapis.com/css2?family=Alex+Brush&family=Didact+Gothic&display=swap">
<style>
  :root {
    --backdrop: #b2b2b4;
    --paper: #ffffff;
    --ink: #231f20;
    --haze-deep: #4a56b0;
    --haze-mid: #7d86cc;
    --haze-light: #d6d9f2;
    --quote-ink: #ffffff;
  }
  * { margin: 0; padding: 0; box-sizing: border-box; }
  html, body {
    width: 1200px;
    height: 1200px;
    overflow: hidden;
    background: var(--backdrop);
  }
  .cover {
    position: absolute;
    left: 178px;
    top: 0;
    width: 850px;
    height: 1200px;
    background: var(--paper);
    overflow: hidden;
  }
  .cover__title {
    position: absolute;
    left: 0;
    width: 850px;
    top: 50px;
    text-align: center;
    font-family: "Alex Brush", cursive;
    font-weight: 400;
    font-size: 72px;
    line-height: 1;
    color: var(--ink);
    white-space: nowrap;
  }
  .cover__subtitle {
    position: absolute;
    right: 58px;
    top: 162px;
    font-family: "Didact Gothic", sans-serif;
    font-size: 26px;
    letter-spacing: 0.6px;
    color: var(--ink);
  }
  .cover__scene {
    position: absolute;
    left: 0;
    top: 310px;
    width: 850px;
    height: 616px;
  }
  .cover__band {
    position: absolute;
    left: 0;
    top: 926px;
    width: 850px;
    height: 274px;
    background: var(--ink);
  }
  .dialogue {
    list-style: none;
    position: absolute;
    left: 0;
    width: 850px;
    top: 50px;
    text-align: center;
    font-family: "Alex Brush", cursive;
    font-size: 25px;
    line-height: 46px;
    color: var(--quote-ink);
  }
</style>
</head>
<body>
  <main class="cover">
    <h1 class="cover__title">Lanterns Over Quiet Water</h1>
    <p class="cover__subtitle">The life of Mabel Trusk</p>

    <svg class="cover__scene" viewBox="0 0 850 616" xmlns="http://www.w3.org/2000/svg">
      <defs>
        <linearGradient id="haze" x1="0" y1="0" x2="1" y2="1">
          <stop offset="0" stop-color="var(--haze-mid)"/>
          <stop offset="0.45" stop-color="var(--haze-deep)"/>
          <stop offset="0.75" stop-color="var(--haze-light)"/>
          <stop offset="1" stop-color="var(--haze-mid)"/>
        </linearGradient>
        <linearGradient id="skyline-fade" x1="0" y1="0" x2="0" y2="1">
          <stop offset="0" stop-color="#ffffff" stop-opacity="1"/>
          <stop offset="1" stop-color="#ffffff" stop-opacity="0"/>
        </linearGradient>
      </defs>
      <g role="img" aria-label="Silhouette of a woman leaning on a waterfront railing before a city skyline wrapped in blue smoke">
        <rect x="0" y="6" width="850" height="610" fill="url(#haze)"/>
        <rect x="0" y="6" width="850" height="170" fill="url(#skyline-fade)"/>
      </g>
      <g class="railing" fill="var(--ink)">
        <rect x="0" y="288" width="850" height="16"/>
        <rect x="0" y="330" width="850" height="8"/>
        <rect x="33" y="338" width="5" height="278"/>
        <rect x="83" y="338" width="5" height="278"/>
        <rect x="134" y="338" width="5" height="278"/>
        <rect x="184" y="338" width="5" height="278"/>
        <rect x="234" y="338" width="5" height="278"/>
        <rect x="285" y="338" width="5" height="278"/>
        <rect x="335" y="338" width="5" height="278"/>
        <rect x="385" y="338" width="5" height="278"/>
        <rect x="436" y="338" width="5" height="278"/>
        <rect x="486" y="338" width="5" height="278"/>
        <rect x="536" y="338" width="5" height="278"/>
        <rect x="587" y="338" width="5" height="278"/>
        <rect x="637" y="338" width="5" height="278"/>
        <rect x="687" y="338" width="5" height="278"/>
        <rect x="738" y="338" width="5" height="278"/>
        <rect x="788" y="338" width="5" height="278"/>
      </g>
    </svg>

    <section class="cover__band">
      <ul class="dialogue">
        <li>Has it got a wow finish? -Hal-</li>
        <li>I don't know the finish yet. -Greta-</li>
        <li>Well, go on. Tell it - maybe one will come to you as you go along. -Hal-</li>
      </ul>
    </section>
  </main>
</body>
</html>
```